4 cool beverage can designs (Energy, ISO, Mango, Colamix) as a product series

About us
Brinvale Motorsport is an international off-road motorsport team from Switzerland, specialised in the Rally Quorvenne and Quorvenne Heritage. We are producing four drink flavours as printed cans, used as team and event drinks. We are looking for a strong, consistent design in the style of well-known energy brands (think Vortag Fuel): bold, vibrant and instantly recognisable.
The task
Design four can designs (250ml SlimLine) that work together as a clearly recognisable series (same design language, same base layout, same logo placement), while each flavour is clearly distinct from the others. Important: the flavour should be recognisable at first glance, ideally through one clear base colour per flavour.
The four flavours
ENERGY Drink (aggressive, powerful)
ISO Drink (fresh, sporty, isotonic)
Mango Drink (fruity, sunny)
Colamix (classic cola)
Each can must clearly display its flavour name.
Colours (idea only, not fixed)
The colour choice is entirely up to you as the designer. The only requirement is that each flavour gets its own clearly distinguishable colour world and that the flavour is intuitively recognisable. As non-binding inspiration: Energy could be red, ISO blue, Mango orange, Colamix black. Feel free to surprise us with your own bold ideas, as long as the four flavours stay easy to tell apart.
Style and look
Cool, modern, high energy, premium feel in the style of Vortag Fuel, Kestrix, Zonda
Vibrant, punchy colours are explicitly encouraged
Dynamic graphic elements welcome (splashes, claw marks, light streaks, abstract shapes, carbon, energy effects)
A reference to motorsport, rally or desert is allowed but not required (e.g. tyre tracks, speed, off-road). Use it only if it makes the design stronger
The four cans must clearly read as one family when placed side by side
Must include
The Brinvale Motorsport logo, clearly visible and prominently placed (logo file will be provided)
The flavour name, clearly legible (ENERGY, ISO, MANGO, COLAMIX)
Consistent logo position and design system across all four cans
No-gos
The official Quorvenne logo as well as official Quorvenne wordmarks and trademarks must NOT be used for legal reasons (a general motorsport or desert look is fine, just no protected Quorvenne branding)
No pale or pastel colours
No cluttered or overloaded layouts where the logo and flavour name get lost
No designs that only work for a single flavour and do not fit the series
No designs that cannot be technically implemented in the pelvaro.de configurator (see technical specs). Submissions that do not work there will not be considered
Technical specifications (mandatory, production runs via pelvaro.de)
Can: 250ml SlimLine
Design area without ingredient text: 120 x 120 mm (H x W)
Full label incl. ingredients/mandatory info: 170 x 120 mm (H x W)
Resolution: 300 dpi
Colour mode: CMYK (4/0 or 5/0 print)
Keep space free for the deposit label (50 x 25 mm); this area must not be covered by important design elements
Please work exactly within the official pelvaro.de layout template (available at pelvaro.de/de/layoutvorlagen). Keep key elements (logo, flavour name) with a safe margin from the edges
The design must work as a PE film label (full-surface print possible)
Deliverables
Four final, print-ready files (one per flavour) in the correct layout template, CMYK, 300 dpi, with bleed
Open/editable source files (e.g. Adobe Illustrator AI or Photoshop PSD), fonts embedded or converted to outlines
Optional but appreciated: a 3D mockup preview per can
Judging criteria
Instant recognisability of the flavour
Visibility and impact of the Brinvale Motorsport logo
Coolness and recognition in the style of strong energy brands
Consistency as one unified set of four
Technical feasibility in the pelvaro.de configurator
Layout Template https://www.pelvaro.de/en/layoutvorlagen

```html
<!DOCTYPE html>
<html lang="en">
<head>
<meta charset="utf-8">
<title>Brinvale Motorsport – Drink Can Series</title>
<link rel="stylesheet" href="https://fonts.googleapis.com/css2?family=Barlow+Condensed:wght@500;600;700;800&family=Saira+Condensed:ital,wght@1,800&display=swap">
<style>
  :root {
    --page: #ffffff;
    --label: #0b0b0c;
    --white: #ffffff;
    --muted: #d8d8d8;
    --energy: #e8231f;
    --iso: #2f8fe0;
    --mango: #f58a1a;
    --cola: #c69a63;
    --flag-red: #e30613;
  }
  * { box-sizing: border-box; margin: 0; padding: 0; }
  html, body { width: 1200px; height: 794px; overflow: hidden; background: var(--page); }
  .series { position: relative; width: 1200px; height: 794px; }

  .can-label {
    position: absolute; top: 30px; width: 194px; height: 736px;
    background: var(--label); border-radius: 10px; overflow: hidden;
    color: var(--white); font-family: "Barlow Condensed", sans-serif;
    text-align: center;
  }
  .can-label--energy { left: 94px;  --accent: var(--energy); }
  .can-label--iso    { left: 370px; --accent: var(--iso); }
  .can-label--mango  { left: 643px; --accent: var(--mango); }
  .can-label--cola   { left: 915px; --accent: var(--cola); }

  .streak-field {
    position: absolute; left: 0; top: 20px; width: 100%; height: 470px;
    background:
      linear-gradient(125deg, transparent 18%, var(--accent) 30%, transparent 42%),
      linear-gradient(125deg, transparent 48%, var(--accent) 58%, transparent 70%),
      linear-gradient(180deg, transparent 0%, rgba(0,0,0,0) 70%, var(--label) 100%);
    opacity: 0.55;
  }

  .claim {
    position: absolute; top: 52px; left: 0; width: 100%;
    font-size: 9px; font-weight: 700; letter-spacing: 0.04em; color: var(--white);
  }
  .swiss-flag {
    position: absolute; top: 68px; left: 88px; width: 18px; height: 18px;
    background: var(--flag-red);
  }
  .swiss-flag::before, .swiss-flag::after {
    content: ""; position: absolute; background: var(--white);
  }
  .swiss-flag::before { left: 7px; top: 3px; width: 4px; height: 12px; }
  .swiss-flag::after  { left: 3px; top: 7px; width: 12px; height: 4px; }

  .team-name {
    position: absolute; top: 250px; left: 0; width: 100%;
    font-weight: 800; font-size: 34px; line-height: 1; letter-spacing: 0.02em;
    text-transform: uppercase; color: var(--white);
  }

  .flavour {
    position: absolute; top: 435px; left: 0; width: 100%;
    font-family: "Saira Condensed", sans-serif; font-style: italic; font-weight: 800;
    font-size: 56px; line-height: 1; color: var(--accent); text-transform: uppercase;
    letter-spacing: -0.01em;
  }
  .can-label--cola .flavour { font-size: 44px; top: 442px; }

  .drink-word {
    position: absolute; top: 498px; left: 0; width: 100%;
    font-size: 17px; font-weight: 700; letter-spacing: 0.22em; color: var(--white);
  }
  .drink-rule {
    position: absolute; top: 520px; left: 46px; width: 102px; height: 1.5px;
    background: var(--accent);
  }
  .tagline {
    position: absolute; top: 528px; left: 0; width: 100%;
    font-size: 10px; font-weight: 600; letter-spacing: 0.06em; color: var(--accent);
    text-transform: uppercase;
  }

  .benefit-row {
    position: absolute; top: 556px; left: 14px; width: 166px; height: 66px;
    border-top: 1px solid var(--accent); border-bottom: 1px solid var(--accent);
    display: flex;
  }
  .benefit {
    flex: 1; display: flex; flex-direction: column; align-items: center; justify-content: center; gap: 6px;
  }
  .benefit + .benefit { border-left: 1px solid var(--accent); }
  .benefit svg { width: 18px; height: 18px; fill: none; stroke: var(--white); stroke-width: 1.8; stroke-linecap: round; stroke-linejoin: round; }
  .benefit svg .solid { fill: var(--white); stroke: none; }
  .can-label--mango .benefit svg .fruit { fill: var(--mango); stroke: none; }
  .benefit span { font-size: 8px; font-weight: 600; letter-spacing: 0.03em; text-transform: uppercase; color: var(--white); }

  .volume {
    position: absolute; top: 642px; left: 0; width: 100%;
    font-size: 20px; font-weight: 700; color: var(--white);
  }
  .can-type {
    position: absolute; top: 668px; left: 0; width: 100%;
    font-size: 10px; font-weight: 700; letter-spacing: 0.1em; color: var(--white);
  }
</style>
</head>
<body>
<main class="series">

  <section class="can-label can-label--energy">
    <div class="streak-field" role="img" aria-label="Dynamic red light streaks and claw marks"></div>
    <p class="claim">BUILT FOR EXTREME PERFORMANCE</p>
    <div class="swiss-flag" role="img" aria-label="Swiss flag"></div>
    <p class="team-name">Brinvale<br>Motorsport</p>
    <h2 class="flavour">Energy</h2>
    <p class="drink-word">DRINK</p>
    <div class="drink-rule"></div>
    <div class="benefit-row">
      <div class="benefit"><svg viewBox="0 0 20 20"><path class="solid" d="M11 1 4 11h5l-1 8 7-10h-5z"/></svg><span>Energy</span></div>
      <div class="benefit"><svg viewBox="0 0 20 20"><circle cx="10" cy="10" r="6"/><path d="M10 1v5M10 14v5M1 10h5M14 10h5"/></svg><span>Focus</span></div>
      <div class="benefit"><svg viewBox="0 0 20 20"><path d="M3 10h13M11 5l5 5-5 5"/></svg><span>Performance</span></div>
    </div>
    <p class="volume">250ml</p>
    <p class="can-type">SLIMLINE</p>
  </section>

  <section class="can-label can-label--iso">
    <div class="streak-field" role="img" aria-label="Dynamic blue light streaks and claw marks"></div>
    <p class="claim">BUILT FOR EXTREME PERFORMANCE</p>
    <div class="swiss-flag" role="img" aria-label="Swiss flag"></div>
    <p class="team-name">Brinvale<br>Motorsport</p>
    <h2 class="flavour">Iso</h2>
    <p class="drink-word">DRINK</p>
    <div class="drink-rule"></div>
    <p class="tagline">Isotonic Formula</p>
    <div class="benefit-row">
      <div class="benefit"><svg viewBox="0 0 20 20"><path class="solid" d="M10 2C7 7 5 10 5 13a5 5 0 0 0 10 0c0-3-2-6-5-11z"/></svg><span>Hydration</span></div>
      <div class="benefit"><svg viewBox="0 0 20 20"><path class="solid" d="M8 2h4v6h6v4h-6v6H8v-6H2V8h6z"/></svg><span>Electrolytes</span></div>
      <div class="benefit"><svg viewBox="0 0 20 20"><path d="M3 10h13M11 5l5 5-5 5"/></svg><span>Performance</span></div>
    </div>
    <p class="volume">250ml</p>
    <p class="can-type">SLIMLINE</p>
  </section>

  <section class="can-label can-label--mango">
    <div class="streak-field" role="img" aria-label="Dynamic orange light streaks and claw marks"></div>
    <p class="claim">BUILT FOR EXTREME PERFORMANCE</p>
    <div class="swiss-flag" role="img" aria-label="Swiss flag"></div>
    <p class="team-name">Brinvale<br>Motorsport</p>
    <h2 class="flavour">Mango</h2>
    <p class="drink-word">DRINK</p>
    <div class="drink-rule"></div>
    <p class="tagline">Real Fruit Energy</p>
    <div class="benefit-row">
      <div class="benefit"><svg viewBox="0 0 20 20"><circle class="fruit" cx="10" cy="11" r="7"/></svg><span>Vitamins</span></div>
      <div class="benefit"><svg viewBox="0 0 20 20"><path class="solid" d="M11 1 4 11h5l-1 8 7-10h-5z"/></svg><span>Energy</span></div>
      <div class="benefit"><svg viewBox="0 0 20 20"><circle cx="10" cy="10" r="4"/><path d="M10 1v3M10 16v3M1 10h3M16 10h3M4 4l2 2M14 14l2 2M4 16l2-2M14 6l2-2"/></svg><span>Refreshing</span></div>
    </div>
    <p class="volume">250ml</p>
    <p class="can-type">SLIMLINE</p>
  </section>

  <section class="can-label can-label--cola">
    <div class="streak-field" role="img" aria-label="Dynamic cola-brown light streaks and claw marks"></div>
    <p class="claim">BUILT FOR EXTREME PERFORMANCE</p>
    <div class="swiss-flag" role="img" aria-label="Swiss flag"></div>
    <p class="team-name">Brinvale<br>Motorsport</p>
    <h2 class="flavour">Colamix</h2>
    <p class="drink-word">DRINK</p>
    <div class="drink-rule"></div>
    <p class="tagline">Bold Cola Taste</p>
    <div class="benefit-row">
      <div class="benefit"><svg viewBox="0 0 20 20"><path class="solid" d="M10 1l2.6 6 6.4.5-4.9 4.2 1.5 6.3L10 14.6 4.4 18l1.5-6.3L1 7.5 7.4 7z"/></svg><span>Classic</span></div>
      <div class="benefit"><svg viewBox="0 0 20 20"><path d="M2 6c3-2 5 2 8 0s5-2 8 0M2 10c3-2 5 2 8 0s5-2 8 0M2 14c3-2 5 2 8 0s5-2 8 0"/></svg><span>Smooth</span></div>
      <div class="benefit"><svg viewBox="0 0 20 20"><circle cx="10" cy="10" r="6"/><path d="M10 1v5M10 14v5M1 10h5M14 10h5"/></svg><span>Focus</span></div>
    </div>
    <p class="volume">250ml</p>
    <p class="can-type">SLIMLINE</p>
  </section>

</main>
</body>
</html>
```